Bramblecove Suite Complementary Pass

I’d like a complimentary pass for any 30-minute Bramblecove Suite session. Choose one of the following options: Infrared Sauna with Red Light, Massage Chair Velquora Compression Therapy, or Paraffin Wax Hand Bath.

Please incorporate the logo and brand colors into your design. I’d like a square image that will be printed on square business cards (no rectangles).

Please refer to the logo and menu for more details.

Contact Information for Business Card

See discretion

```html
<!DOCTYPE html>
<html lang="en">
<head>
<meta charset="UTF-8">
<title>Bramblecove Suite Complimentary Pass</title>
<link href="https://fonts.googleapis.com/css2?family=Bebas+Neue&family=Dancing+Script:wght@700&family=Nunito:wght@400;600;700;800&display=swap" rel="stylesheet">
<style>
  :root {
    --stage: #979797;
    --violet: #472c8a;
    --coral: #f06a4a;
    --paper: #fbfaf8;
    --white: #ffffff;
  }
  * { margin: 0; padding: 0; box-sizing: border-box; }
  html, body { width: 1200px; height: 1000px; overflow: hidden; }
  body {
    background: var(--stage);
    position: relative;
    font-family: "Nunito", sans-serif;
  }
  .card {
    position: absolute;
    width: 520px;
    height: 520px;
    box-shadow: 0 14px 22px rgba(0,0,0,0.28);
  }
  .card-front {
    left: 70px; top: 267px;
    background: var(--violet);
    border-top-left-radius: 46px;
    text-align: center;
    color: var(--white);
  }
  .card-back {
    left: 610px; top: 269px;
    background: var(--paper);
    border-top-right-radius: 46px;
  }
  .pass-intro {
    position: absolute;
    top: 146px; left: 0; width: 520px;
    font-size: 18px;
    font-weight: 600;
  }
  .pass-title {
    position: absolute;
    top: 174px; left: 58px; width: 404px;
    font-family: "Bebas Neue", sans-serif;
    font-size: 90px;
    font-weight: 400;
    line-height: 1;
    color: var(--coral);
    letter-spacing: 0.5px;
    transform: scaleY(1.28);
    transform-origin: top center;
    white-space: nowrap;
  }
  .pass-subtitle {
    position: absolute;
    top: 248px; left: 0; width: 520px;
    font-family: "Dancing Script", cursive;
    font-weight: 700;
    font-size: 54px;
    line-height: 1;
    color: var(--white);
  }
  .brand {
    display: flex;
    align-items: center;
    gap: 10px;
    font-weight: 700;
    font-size: 26px;
    line-height: 1;
  }
  .brand-dot {
    width: 20px; height: 20px;
    border-radius: 50%;
    flex: none;
    background: var(--coral);
  }
  .card-front .brand {
    position: absolute;
    top: 393px; left: 0; width: 520px;
    justify-content: center;
    color: var(--white);
  }
  .options-heading {
    position: absolute;
    top: 78px; left: 62px;
    font-size: 20px;
    font-weight: 800;
    color: var(--coral);
  }
  .options-list {
    position: absolute;
    top: 155px; left: 62px;
    list-style: none;
    color: var(--violet);
    font-size: 22px;
    line-height: 28px;
  }
  .options-list li {
    position: relative;
    padding-left: 17px;
    margin-bottom: 30px;
  }
  .options-list li::before {
    content: "";
    position: absolute;
    left: 0; top: 11px;
    width: 8px; height: 8px;
    border-radius: 50%;
    background: var(--violet);
  }
  .card-back .brand {
    position: absolute;
    top: 397px; left: 66px;
    color: var(--violet);
  }
</style>
</head>
<body>
  <section class="card card-front">
    <p class="pass-intro">I’d like a complimentary pass for any 30-minute</p>
    <h1 class="pass-title">Bramblecove</h1>
    <p class="pass-subtitle">Suite Session</p>
    <div class="brand"><span class="brand-dot"></span>solvane physical therapy</div>
  </section>

  <section class="card card-back">
    <h2 class="options-heading">Choose one of the following options:</h2>
    <ul class="options-list">
      <li>Infrared Sauna with Red Light</li>
      <li>Massage Chair Velquora<br>Compression Therapy</li>
      <li>Paraffin Wax Hand Bath.</li>
    </ul>
    <div class="brand"><span class="brand-dot"></span>solvane physical therapy</div>
  </section>
</body>
</html>
```